Town Planning Consultants require lstationary design

Require a design to be used for our letterhead and report cover page. We have an approved logo.
we have attached our logo, and our temporary letterhead/cover page (SEE Cover) which we currently adapt for both purposes in the interim pending a permanent design. I have also attached an example (example report cover) of a report cover page that I like. perhaps similar with our colour scheme

Target Market(s)

?

Industry/Entity Type

Town

Colors
249fd4
3176b5

Requirements
Must have
• colours to match logo
• the text content in existing letterhead

```html
<!DOCTYPE html>
<html lang="en">
<head>
<meta charset="utf-8">
<title>Ashcombe Planning Letterhead</title>
<link rel="stylesheet" href="https://fonts.googleapis.com/css2?family=Roboto:wght@400;500&display=swap">
<style>
  :root {
    --brand-blue: #249fd4;
    --brand-deep: #3176b5;
    --ink: #2b2b2b;
    --muted: #555555;
    --grey-band: #8a8b8e;
    --paper: #ffffff;
    --backdrop: #e7e8ea;
  }
  * { box-sizing: border-box; margin: 0; padding: 0; }
  html, body { width: 1200px; height: 800px; overflow: hidden; }
  body {
    background: var(--backdrop);
    font-family: "Roboto", Arial, sans-serif;
    color: var(--ink);
  }
  .letterhead {
    position: absolute;
    left: 330px; top: 18px;
    width: 540px; height: 764px;
    background: var(--paper);
    box-shadow: 0 2px 10px rgba(0,0,0,0.12);
    overflow: hidden;
  }
  .letterhead__header {
    position: absolute;
    left: 38px; right: 34px; top: 30px;
    height: 78px;
    border-bottom: 1px solid var(--brand-blue);
  }
  .brand {
    position: absolute;
    left: 0; bottom: 8px;
  }
  .brand__name {
    font-size: 24px;
    font-weight: 500;
    line-height: 1;
    color: var(--ink);
    letter-spacing: 0.3px;
  }
  .contact {
    position: absolute;
    right: 0; bottom: 6px;
    list-style: none;
    font-size: 6.5px;
    line-height: 10px;
    color: var(--muted);
    text-align: right;
  }
  .contact li { display: flex; justify-content: flex-end; align-items: center; gap: 4px; }
  .contact__icon {
    width: 6px; height: 6px; border-radius: 50%;
    background: var(--brand-blue);
  }
  .letter-body {
    position: absolute;
    left: 60px; right: 56px; top: 150px;
    font-size: 10.5px;
    line-height: 15px;
    letter-spacing: 0.4px;
  }
  .letter-body__salutation {
    font-weight: 500;
    margin-bottom: 18px;
  }
  .letter-body p { margin-bottom: 16px; }
  .letterhead__footer {
    position: absolute;
    left: 0; bottom: 0;
    width: 540px; height: 44px;
  }
  .tagline {
    position: absolute;
    left: 12px; bottom: 3px;
    font-size: 8.5px;
    line-height: 10px;
    color: #ffffff;
    letter-spacing: 0.6px;
  }
</style>
</head>
<body>
  <main class="letterhead">
    <header class="letterhead__header">
      <div class="brand">
        <span class="brand__name">Ashcombe Planning</span>
      </div>
      <ul class="contact">
        <li>12 Harbour Lane, Rivermead <span class="contact__icon"></span></li>
        <li>Tel 555 0142 <span class="contact__icon"></span></li>
        <li>Fax 555 0143 <span class="contact__icon"></span></li>
        <li>info@ashcombeplan.example <span class="contact__icon"></span></li>
      </ul>
    </header>

    <section class="letter-body">
      <p class="letter-body__salutation">Dear sir,</p>
      <p>The main body should clearly state the points that you want to make. As a general rule it is a good idea to keep this as to the point as possible to ensure that the recipient remains engaged. A longer main body may be more appropriate when making a complaint as you may require to add more detail in order to convey the importance of what you are putting across.</p>
      <p>The main body should clearly state the points that you want to make. As a general rule it is a good idea to keep this as to the point as possible to ensure that the recipient remains engaged. A longer main body may be more appropriate</p>
      <p>The main body should clearly state the points that you want to make. As a general rule it is a good idea to keep this as to the point as possible to ensure that the recipient remains engaged. A longer main body may be more appropriate when making a complaint as you may require to add more detail in order to convey the importance of what you are putting across.</p>
      <p>The main body should clearly state the points that you want to make. As a general rule it is a good idea to keep this as to the point as possible to ensure that the recipient remains engaged. A longer main body may be more appropriate when making a complaint as you may require to add more detail in order to convey the importance of what you are putting across.</p>
      <p>The main body should clearly state the points that you want to make. As a general rule it is a good idea to keep this as to the point as possible to ensure that the recipient remains engaged. A longer main body may be more appropriate</p>
    </section>

    <footer class="letterhead__footer">
      <svg width="540" height="44" viewBox="0 0 540 44" aria-hidden="true">
        <polygon points="430,6 540,6 540,30 404,30" fill="var(--grey-band)"/>
        <polygon points="0,30 540,30 540,44 0,44" fill="var(--brand-blue)"/>
        <polygon points="404,30 414,30 408,36 398,36" fill="var(--brand-deep)" opacity="0.6"/>
      </svg>
      <span class="tagline">• Planning • Development • Urban Design • Consultants</span>
    </footer>
  </main>
</body>
</html>
```